Epoxy Flooring Contractor business card

We need a business card to promote a new addition to our business. We now offer Epoxy Flooring. We would like for the business card to include the images attached. One is our logo, the other is a sample of metallic epoxy flooring, we would like to incorporate that somewhere into the design. I was thinking an icon of a man pushing a concrete grinder and have the color set to the metallic epoxy color. I found a business card sample on this website, I will attach it. It has the icon that we are looking for, or something similar.
Our company name is Brightmore Coatings LLC
Our owners name is Dana Pellow
Phone is 561-847-2916
website is www.brightmore-coatingsllc.com
please let me know if you need any other info

Contact Information for Business Card

Brightmore Coatings LLC
Dana Pellow, owner
Phone: 561-847-2916
Address: P.O Box 8146 Lake Worth, FL 33471
www.Brightmore-CoatingsLLC.com
BrightmoreCoatingsLLC@mailvista.net
Include logo attached
It must include a Clip art of man with concrete grinder
Must include metallic epoxy design attached
Must include the following text
Residential Garage Flooring
Epoxy Countertops
Commercial Epoxy Flooring
Restaurant Flooring
Warehouse Flooring
Licensed & Insured
Free Estimates

Colors

Designer to choose colors to be used in the design.

Requirements
Must have
• Include logo attached
• It must include a Clip art of man with concrete grinder
• Must include metallic epoxy design attached
• Must include the following text
• Garage Epoxy Flooring
• Residential Epoxy Flooring
• Concrete Floor Crack Repairs
• Concrete Floor Grinding
• Commercial & Warehouse Epoxy Flooring
• Restaurant Epoxy Flooring
• Epoxy Countertops
• Non Slip Epoxy Pool Decks
• Textured Finishes, Flakes, Granite Coat, Metallic & Quartz
• FREE ESTIMATES • LICENSED & INSURED

```html
<!DOCTYPE html>
<html lang="en">
<head>
<meta charset="utf-8">
<title>Brightmore Coatings LLC – Business Card</title>
<link href="https://fonts.googleapis.com/css2?family=Roboto:wght@400;500&family=Roboto+Condensed:wght@400;500&display=swap" rel="stylesheet">
<style>
  :root {
    --page-bg: #9a9a9a;
    --card-white: #ffffff;
    --flake-dark: #2f3236;
    --flake-mid: #6d7176;
    --flake-blue: #2b5aa8;
    --brand-blue: #3d5f8e;
    --brand-light: #7da3cf;
    --rule-blue: #5b7aa5;
    --text-grey: #555a60;
    --ghost-grey: #eceef0;
  }
  * { box-sizing: border-box; margin: 0; padding: 0; }
  html, body { width: 1200px; height: 930px; overflow: hidden; }
  body {
    background: var(--page-bg);
    font-family: "Roboto", Arial, sans-serif;
    position: relative;
  }
  .card {
    position: absolute;
    left: 300px;
    width: 600px;
    height: 343px;
    border-radius: 22px;
    overflow: hidden;
  }
  /* ---------- back side ---------- */
  .card-back { top: 100px; }
  .flake-surface {
    position: absolute; inset: 0;
    background:
      radial-gradient(circle at 30% 40%, rgba(43,90,168,0.35), transparent 45%),
      radial-gradient(circle at 75% 70%, rgba(43,90,168,0.25), transparent 40%),
      linear-gradient(135deg, var(--flake-mid), var(--flake-dark) 55%, var(--flake-mid));
  }
  .brand {
    position: absolute;
    display: flex; align-items: center;
  }
  .brand-square { flex: none; }
  .brand-name { font-weight: 500; letter-spacing: 1px; }
  .back-brand {
    left: 0; right: 0; top: 88px;
    justify-content: center; gap: 14px;
  }
  .back-brand .brand-square { width: 44px; height: 44px; background: #8fb4dc; }
  .back-brand .brand-name { color: #ffffff; font-size: 28px; line-height: 30px; }
  .services {
    position: absolute;
    left: 0; right: 0; top: 200px;
    text-align: center;
    color: #ffffff;
    font-size: 15px;
    line-height: 22px;
    letter-spacing: 0.6px;
  }
  /* ---------- front side ---------- */
  .card-front { top: 487px; background: var(--card-white); }
  .grinder-art {
    position: absolute;
    left: 225px; top: 30px;
    width: 200px; height: 290px;
    border-radius: 40px;
    background: linear-gradient(180deg, var(--ghost-grey), #f6f7f8);
  }
  .front-brand {
    left: 40px; top: 150px;
    gap: 10px;
  }
  .front-brand .brand-square { width: 38px; height: 38px; background: var(--brand-light); }
  .front-brand .brand-name {
    color: var(--brand-blue);
    font-size: 24px; line-height: 26px;
  }
  .divider {
    position: absolute;
    left: 300px; top: 72px;
    width: 1.5px; height: 200px;
    background: var(--rule-blue);
  }
  .contact {
    position: absolute;
    left: 322px; top: 70px;
    font-family: "Roboto Condensed", Arial, sans-serif;
    color: var(--text-grey);
  }
  .contact .person-name {
    color: var(--brand-blue);
    font-size: 30px; font-weight: 500;
    letter-spacing: 0.5px;
    line-height: 32px;
  }
  .contact .person-role { font-size: 15px; margin: 4px 0 12px; }
  .contact .address { font-size: 15px; line-height: 20px; margin-bottom: 10px; }
  .contact ul { list-style: none; }
  .contact li {
    display: flex; align-items: center; gap: 8px;
    font-size: 15px; line-height: 22px;
  }
  .contact li svg { width: 12px; height: 12px; flex: none; }
</style>
</head>
<body>

<section class="card card-back">
  <div class="flake-surface" role="img" aria-label="Grey, black and blue epoxy flake floor texture"></div>
  <div class="brand back-brand">
    <span class="brand-square"></span>
    <span class="brand-name">Brightmore<br>Coatings</span>
  </div>
  <p class="services">
    Residential Garage Flooring | Epoxy Countertops<br>
    Commercial Epoxy Flooring | Restaurant Flooring<br>
    Warehouse Flooring | Licensed &amp; Insured | Free Estimates
  </p>
</section>

<section class="card card-front">
  <div class="grinder-art" role="img" aria-label="Faint clip art of a man pushing a concrete grinder"></div>
  <div class="brand front-brand">
    <span class="brand-square"></span>
    <span class="brand-name">Brightmore<br>Coatings</span>
  </div>
  <div class="divider"></div>
  <div class="contact">
    <h1 class="person-name">DANA PELLOW</h1>
    <p class="person-role">Owner</p>
    <p class="address">P.O Box 8146 Lake<br>Worth, FL 33471</p>
    <ul>
      <li>
        <svg viewBox="0 0 12 12"><path d="M2.5 1l2 2-1 1.3c.6 1.4 1.8 2.6 3.2 3.2l1.3-1 2 2-1.2 1.5C5.6 9.8 2.2 6.4 1 2.2z" fill="#3d5f8e"/></svg>
        561-847-2916
      </li>
      <li>
        <svg viewBox="0 0 12 12"><rect x="1" y="2.5" width="10" height="7" fill="none" stroke="#3d5f8e" stroke-width="1.2"/><path d="M1 2.5l5 4 5-4" fill="none" stroke="#3d5f8e" stroke-width="1.2"/></svg>
        BrightmoreCoatingsLLC@mailvista.net
      </li>
      <li>
        <svg viewBox="0 0 12 12"><circle cx="6" cy="6" r="5" fill="none" stroke="#3d5f8e" stroke-width="1.2"/><path d="M1 6h10M6 1c-2.5 3-2.5 7 0 10M6 1c2.5 3 2.5 7 0 10" fill="none" stroke="#3d5f8e" stroke-width="1"/></svg>
        www.Brightmore-CoatingsLLC.com
      </li>
    </ul>
  </div>
</section>

</body>
</html>
```